Revamp of current landing page for high conversions

I need to revamp my current landing pages and I want to see designs that incorporate elements from both of these current designs... http://www.brightmarlowsmilestudio.com/

https://qrtvwm.pagefunnelo.co/revu-glowpackbox42/

Please implement these images into the design: https://www.snapgallo.com/p/QXR7Lm2K_Z-/?taken-by=brightmarlowsmilestudio

https://www.snapgallo.com/p/QW8TrjMnpvD/?taken-by=brightmarlowsmilestudio

https://www.snapgallo.com/p/QWzhDkpm3_R/?taken-by=brightmarlowsmilestudio

https://www.snapgallo.com/p/QWfomJTpQAx/?taken-by=brightmarlowsmilestudio

https://www.snapgallo.com/p/QWfgn73pr-t/?taken-by=brightmarlowsmilestudio

https://www.snapgallo.com/p/QWcRtKYGwMn/?taken-by=brightmarlowsmilestudio

https://www.snapgallo.com/p/QWVjf9jpkr5/?taken-by=brightmarlowsmilestudio

https://www.snapgallo.com/p/QWDmvX4GhWz/?taken-by=brightmarlowsmilestudio

https://www.snapgallo.com/p/QV5h8WnG2P7/?taken-by=brightmarlowsmilestudio

Target Market(s)

People that care about their looks and who want whiter teeth. People that are interested in good oral hygeine

Industry/Entity Type

Dental Clinic

Number of Pages Required

1 page

Colors

Designer to choose colors to be used in the design.

Requirements
Must have
• images of my customers that I have included in the description.
• Also, I would like to see a professional laser teeth whitening treatment that happens in dental office and make emphasis on FREE HOME MAINTENANCE KIT INCLUDED!
• Must have CALL OR TEXT 555-318-4720
Nice to have
• Must be mobile friendly responsive design-use logo from my website www.brightmarlowsmilestudo.com
Should not have
• stock images of people I dont like stock images of people so please use the images from my instagram account

```html
<!DOCTYPE html>
<html lang="en">
<head>
<meta charset="utf-8">
<title>Bright Marlow Smile Studio – $99 Laser Teeth Whitening</title>
<link href="https://fonts.googleapis.com/css2?family=Roboto:ital,wght@0,300;0,400;0,500;0,700;1,300;1,400&display=swap" rel="stylesheet">
<style>
:root{
  --blue:#05a9ec;
  --blue-deep:#0a8fd6;
  --blue-soft:#bfe6fa;
  --blue-pale:#e6f5fd;
  --ink:#3b3b3b;
  --muted:#6d6d6d;
  --white:#ffffff;
}
*{box-sizing:border-box;margin:0;padding:0}
html,body{width:1061px;height:1200px;overflow:hidden;background:var(--white)}
body{font-family:"Roboto",Arial,sans-serif;color:var(--ink);position:relative}
.abs{position:absolute}

/* header */
.site-header{left:0;top:0;width:1061px;height:90px;background:var(--white);box-shadow:0 2px 6px rgba(0,0,0,.12);z-index:3}
.brand{left:225px;top:26px;display:flex;align-items:center;gap:10px}
.brand-dot{width:40px;height:40px;border-radius:50%;background:var(--blue-pale);border:2px solid var(--blue-soft)}
.brand-name{font-size:20px;font-weight:500;color:var(--blue-deep);line-height:1.05;width:180px}
.contact{top:20px;text-align:center;color:var(--blue);font-size:12px;font-weight:500}
.contact svg{display:block;margin:0 auto 6px}
.contact.phone{left:618px;width:92px}
.contact.location{left:752px;width:88px}
.header-divider{left:731px;top:20px;width:1px;height:46px;background:var(--blue-soft)}

/* hero */
.hero{left:0;top:90px;width:1061px;height:329px;background:var(--white)}
.hero-photos{left:477px;top:90px;width:584px;height:329px;
  background:linear-gradient(135deg,#4ab9ec 0%,#7fcdf1 35%,#3aaee6 65%,#8ad2f2 100%)}
.hero-copy{left:251px;top:116px;width:240px;text-align:center}
.hero-kicker{font-size:8px;color:var(--muted)}
.hero-price{display:flex;justify-content:center;align-items:center;gap:4px;margin-top:6px}
.hero-price strong{font-size:58px;font-weight:700;color:var(--blue);line-height:1}
.hero-title{font-size:21px;font-weight:500;color:var(--blue);line-height:1.2;margin-top:4px}
.hero-note{font-size:7.5px;color:var(--muted);margin-top:10px;line-height:1.4}
.hero-call{font-size:9px;color:var(--blue);margin-top:26px;line-height:1.35}
.cta{display:inline-flex;align-items:center;gap:14px;margin-top:8px;background:var(--blue);color:var(--white);
  font-size:13px;font-weight:700;border-radius:18px;padding:8px 24px 8px 12px}
.hero-fine{font-size:7.5px;color:var(--muted);margin-top:9px}

/* how it works */
.how{left:0;top:419px;width:1061px;height:220px;background:var(--blue)}
.how-copy{left:252px;top:436px;width:272px;color:var(--white)}
.how-copy h2{font-size:32px;font-weight:400;line-height:1}
.how-lead{font-size:10.5px;font-style:italic;margin-top:10px;line-height:1.3}
.how-lead b{font-weight:700}
.how-body{font-size:12.5px;font-weight:300;margin-top:14px;line-height:1.25}

.price-card{left:569px;top:385px;width:216px;height:285px;background:var(--white);box-shadow:0 2px 8px rgba(0,0,0,.18);text-align:center;padding-top:22px;z-index:2}
.price-card .tag{font-size:13px;font-style:italic;font-weight:300;color:var(--ink);line-height:1.35}
.price-card .for{font-size:19px;font-weight:500;color:var(--blue);margin-top:8px}
.price-card .big{font-size:82px;font-weight:500;color:var(--blue);line-height:1;margin-top:2px}
.price-card .save{font-size:13px;font-style:italic;font-weight:300;line-height:1.35;margin-top:10px}
.price-card .occasion{font-size:8px;color:var(--ink);line-height:1.5;margin-top:14px;padding:0 22px}

/* features band (drawn beneath the testimonial card) */
.features{left:0;top:855px;width:1061px;height:345px;background:var(--blue);z-index:0}

/* testimonial */
.testimonial-photos{left:0;top:639px;width:1061px;height:216px;
  background:linear-gradient(90deg,#cbc6c2 0%,#d9d5d1 40%,#c2bdba 70%,#d5d1ce 100%)}
.testimonial-card{left:330px;top:700px;width:401px;height:210px;background:var(--white);border-radius:16px;box-shadow:0 2px 8px rgba(0,0,0,.2);text-align:center;padding:40px 44px 0;z-index:2}
.quote-badge{left:500px;top:669px;width:60px;height:60px;border-radius:50%;background:var(--blue);z-index:3}
.testimonial-card p{font-size:10.5px;font-style:italic;font-weight:300;color:var(--muted);line-height:1.35}
.testimonial-card hr{border:0;border-top:1px solid #cfcfcf;width:180px;margin:18px auto 10px}
.testimonial-card .author{font-size:12px;font-weight:500;color:var(--blue)}
.testimonial-card .author span{font-weight:400}

/* features content */
.features-title{left:252px;top:938px;font-size:32px;font-weight:400;color:var(--white);z-index:1}
.feature-labels{left:260px;top:1000px;width:115px;text-align:right;color:var(--white);font-size:11.5px;font-weight:500;z-index:1}
.feature-labels li{list-style:none;height:27.5px;line-height:22px}
.plan{top:941px;width:104px;height:199px;border-radius:10px;overflow:hidden;background:linear-gradient(180deg,#a7dbf5,#eaf7fd);z-index:1}
.plan-head{height:47px;background:var(--white);display:flex;align-items:center;justify-content:center;text-align:center;
  color:var(--blue);font-size:17px;font-weight:400;line-height:1;border-bottom:2px solid var(--blue)}
.plan-head.own{font-size:11px;font-weight:500;gap:5px}
.plan-head.own i{width:16px;height:16px;border-radius:50%;background:var(--blue-pale);border:1px solid var(--blue-soft);flex:none}
.plan ul{list-style:none;padding-top:13px}
.plan li{height:27.5px;line-height:24px;padding-left:8px;font-size:8px;color:var(--ink);border-bottom:1px solid rgba(255,255,255,.85);background:linear-gradient(90deg,rgba(255,255,255,.85),rgba(255,255,255,.25))}
</style>
</head>
<body>

<header class="abs site-header">
  <div class="abs brand"><span class="brand-dot"></span><span class="brand-name">Bright Marlow Smile Studio</span></div>
  <div class="abs contact phone">
    <svg width="22" height="22" viewBox="0 0 24 24" fill="none" stroke="#05a9ec" stroke-width="1.6"><path d="M5 3h4l2 5-2.5 1.5a11 11 0 0 0 6 6L16 13l5 2v4a2 2 0 0 1-2 2A17 17 0 0 1 3 5a2 2 0 0 1 2-2z"/></svg>
    1-555-318-4721
  </div>
  <div class="abs header-divider"></div>
  <div class="abs contact location">
    <svg width="22" height="22" viewBox="0 0 24 24" fill="none" stroke="#05a9ec" stroke-width="1.6"><path d="M12 22s7-7 7-12a7 7 0 0 0-14 0c0 5 7 12 7 12z"/><circle cx="12" cy="10" r="2.5"/></svg>
    Harbor Point
  </div>
</header>

<section class="abs hero"></section>
<div class="abs hero-photos" role="img" aria-label="Grid of blue-tinted customer photos holding smile signs"></div>
<div class="abs hero-copy">
  <div class="hero-kicker">$378 Teeth Whitening System For Only</div>
  <div class="hero-price"><strong>$99</strong>
    <svg width="46" height="46" viewBox="0 0 46 46" fill="none" stroke="#05a9ec" stroke-width="2.4"><rect x="3" y="7" width="32" height="28" rx="3"/><path d="M3 15h32M11 3v8M27 3v8"/><circle cx="31" cy="31" r="11" fill="#fff"/><path d="M31 25v6l4 3"/></svg>
  </div>
  <div class="hero-title">LASER TEETH<br>WHITENING DEAL</div>
  <div class="hero-note">Our exclusive "Triple Treatment"<br>plus one take home maintenance kit</div>
  <div class="hero-call">Call or text to book 1-555-318-4720<br>or click below to get the deal</div>
  <div class="cta">
    <svg width="18" height="18" viewBox="0 0 20 20" fill="none" stroke="#fff" stroke-width="1.6"><circle cx="10" cy="10" r="8.5"/><path d="M6 10h8M11 7l3 3-3 3"/></svg>
    GET THIS DEAL NOW
  </div>
  <div class="hero-fine">* Limited Appointments available - print free coupon</div>
</div>

<section class="abs how"></section>
<div class="abs how-copy">
  <h2>How it Works</h2>
  <p class="how-lead"><b>Why pay hundreds of dollars</b> when you can get a professional teeth whitening procedure for much less than your local dentist office?</p>
  <p class="how-body">We utilize the latest Blue Light Whitening Technology in combination with our Hydrogen Peroxide Whitening Gel to accelerate the whitening process! It's effective, safe and affordable! With our treatment your smile will be noticeably whiter in less than an hour!</p>
</div>

<aside class="abs price-card">
  <div class="tag">Affordable Teeth Whitening<br>in Bayview</div>
  <div class="for">for only</div>
  <div class="big">$99</div>
  <div class="save">Save Hundreds vs<br>Going To Your Local Dentist!</div>
  <div class="occasion">Get ready For High School Prom, Mother's Day, Graduation, Wedding, Vacation, or any Occasion.</div>
</aside>

<div class="abs testimonial-photos" role="img" aria-label="Customers holding smile signs in front of the studio backdrop"></div>
<section class="abs features"></section>

<div class="abs quote-badge">
  <svg width="60" height="60" viewBox="0 0 60 60" fill="#fff"><path d="M17 38c0-9 3-14 10-17l1 3c-4 2-5 4-5 7h5v10H17zM33 38c0-9 3-14 10-17l1 3c-4 2-5 4-5 7h5v10H33z"/></svg>
</div>
<blockquote class="abs testimonial-card">
  <p>"So I just had my teeth whitened using the blue laser light and I have to say this was one of the best experiences I've had with teeth whitening. Daniela (the women who helped me) was very clear about the process and walked me through each ste. I would say the whole process took about 45-60 minutes. After the teeth whitening process was finished I could tell immediately and I was very pleased with the end results."</p>
  <hr>
  <div class="author">Marcus T. <span>Bayview, CA</span></div>
</blockquote>

<h2 class="abs features-title">Features</h2>
<ul class="abs feature-labels">
  <li>SPEED</li><li>EASE OF USE</li><li>COST</li><li>TIME REQUIREMENTS</li><li>AVAILABILITY</li>
</ul>

<div class="abs plan" style="left:395px">
  <div class="plan-head own"><i></i>Bright Marlow</div>
  <ul><li>Results in 45 minutes</li><li>Very easy</li><li>$378</li><li>Less than an hour</li><li>Walk in &amp; By Appt</li></ul>
</div>
<div class="abs plan" style="left:507px">
  <div class="plan-head">GLEAMPRO</div>
  <ul><li>Results in 3 Treatments</li><li>Difficult/Dentist</li><li>$600-$1000</li><li>3 Hours</li><li>By Apointment Only</li></ul>
</div>
<div class="abs plan" style="left:618px">
  <div class="plan-head">LUMA<br>SMILE</div>
  <ul><li>Results in 1 hour</li><li>Difficult/Dentist</li><li>$399-$600</li><li>1 Hour + Home Treatment</li><li>By Apointment Only</li></ul>
</div>
<div class="abs plan" style="left:729px">
  <div class="plan-head">OTHER</div>
  <ul><li>7-10 Days</li><li>Self</li><li>$50-$150</li><li>Nightly 7-30 Days</li><li>Store Purchase</li></ul>
</div>

</body>
</html>
```